I need business cards for a company that will be an umbrella for many retail stores. I need them to be sleek and modern. I would like some white and black in the background of the card as these are the office colours the logo is attached.
Target Market(s)
worldwide
Industry/Entity Type
Business
Requirements
Must have
- traditional business card shape
Should not have
- too many colours
no swirly text

```html
<!DOCTYPE html>
<html lang="en">
<head>
<meta charset="utf-8">
<title>Nira General Trading – Business Cards</title>
<link rel="stylesheet" href="https://fonts.googleapis.com/css2?family=Cinzel:wght@400;500;600&display=swap">
<style>
  :root {
    --page-bg: #e9e9e9;
    --card-top: #ffffff;
    --card-bottom: #efefef;
    --ink: #1e1e1e;
    --base-band: #111111;
    --stripe-dark: #1f5aa6;
    --stripe-light: #c3cbe6;
    --accent: #1f5aa6;
  }
  * { box-sizing: border-box; margin: 0; padding: 0; }
  html, body {
    width: 1200px;
    height: 1200px;
    overflow: hidden;
    background: var(--page-bg);
    font-family: "Cinzel", Georgia, serif;
    color: var(--ink);
  }
  .canvas { position: relative; width: 1200px; height: 1200px; }

  .card {
    position: absolute;
    left: 247px;
    width: 720px;
    height: 427px;
    background: linear-gradient(180deg, var(--card-top) 0%, var(--card-bottom) 100%);
    border-radius: 8px;
    box-shadow: 0 6px 18px rgba(0, 0, 0, 0.18);
    overflow: hidden;
  }
  .card--front { top: 137px; }
  .card--back  { top: 664px; }

  .card__base-band {
    position: absolute;
    left: 0;
    right: 0;
    bottom: 0;
    height: 34px;
    background: var(--base-band);
  }

  .card__stripe { position: absolute; top: 0; bottom: 0; }
  .card__stripe--outer-left  { left: 36px; width: 5px; background: var(--stripe-light); }
  .card__stripe--centre      { left: 45px; width: 5px; background: var(--stripe-dark); }
  .card__stripe--outer-right { left: 55px; width: 5px; background: var(--stripe-light); }

  .brand {
    position: absolute;
    display: flex;
    align-items: center;
    color: var(--ink);
    font-weight: 400;
  }
  .brand__dot { border-radius: 50%; background: var(--accent); flex: none; }
  .brand__name { line-height: 1.15; white-space: nowrap; }
  .brand__line { display: block; }

  .brand--large { left: 200px; top: 160px; gap: 22px; }
  .brand--large .brand__dot { width: 64px; height: 64px; }
  .brand--large .brand__line--main { font-size: 32px; }
  .brand--large .brand__line--sub  { font-size: 23px; letter-spacing: 0.5px; }

  .brand--small { left: 100px; top: 28px; gap: 12px; }
  .brand--small .brand__dot { width: 34px; height: 34px; }
  .brand--small .brand__line--main { font-size: 19px; }
  .brand--small .brand__line--sub  { font-size: 14px; letter-spacing: 0.3px; }

  .contact-fields {
    position: absolute;
    left: 135px;
    top: 140px;
    list-style: none;
  }
  .contact-fields__label {
    font-size: 20px;
    font-weight: 600;
    height: 57px;
    letter-spacing: 0.3px;
  }
</style>
</head>
<body>
<main class="canvas">

  <section class="card card--front" aria-label="Business card front">
    <span class="card__stripe card__stripe--outer-left"></span>
    <span class="card__stripe card__stripe--centre"></span>
    <span class="card__stripe card__stripe--outer-right"></span>
    <span class="card__base-band"></span>
    <div class="brand brand--large">
      <span class="brand__dot"></span>
      <span class="brand__name">
        <span class="brand__line brand__line--main">Nira</span>
        <span class="brand__line brand__line--sub">General Trading</span>
      </span>
    </div>
  </section>

  <section class="card card--back" aria-label="Business card back">
    <span class="card__stripe card__stripe--outer-left"></span>
    <span class="card__stripe card__stripe--centre"></span>
    <span class="card__stripe card__stripe--outer-right"></span>
    <span class="card__base-band"></span>
    <div class="brand brand--small">
      <span class="brand__dot"></span>
      <span class="brand__name">
        <span class="brand__line brand__line--main">Nira</span>
        <span class="brand__line brand__line--sub">General Trading</span>
      </span>
    </div>
    <ul class="contact-fields">
      <li class="contact-fields__label">Name :</li>
      <li class="contact-fields__label">post office box:</li>
      <li class="contact-fields__label">Telephone:</li>
      <li class="contact-fields__label">e-mail:</li>
    </ul>
  </section>

</main>
</body>
</html>
```